Consulting Website

We are looking at renewing out company's website. we are an organizational development consulting firm that works within the Middle East and Africa. Our focus on on organizations within the Gulf area.

We are looking to having a simple, clean and attractive website. pictures should be relevant to our location.

We are also looking for a creative design, something that isn't just "another consulting website"
Updates

Thank you all for submitting your designs, following are some general comments;

- Having a veiled women on the intro is NOT a must
- have a picture with people is NOT a must too, we can use nature, symbols, places..anything really!
- Here are some sites i like;
mivanorth.example
http://www.brellokhomes.example/
http://www.quistavarn.example/
http://www.zorebin.example/

I hope these could give you some idea :)

thanks again.

Industry/Entity Type

It Company

Requirements
Must have
• Tabs for press, testimonials, products, resources and services.
pictures also should be relevant to the geographical location. i.e. veiled women, men in traditional costumes and so on.

It's very important that we MAINTAIN the corporate colors of the logo.
Should not have
• Clean and neat design!
i REALLY dont like crowded designs.

```html
<!DOCTYPE html>
<html lang="en">
<head>
<meta charset="utf-8">
<title>Velmora Consulting – About</title>
<link rel="stylesheet" href="https://fonts.googleapis.com/css2?family=PT+Sans:wght@400;700&family=Source+Sans+3:wght@400;600&display=swap">
<style>
  :root {
    --page-bg: #ededed;
    --panel: #ffffff;
    --ink: #4a4a50;
    --heading: #2a2f45;
    --brand-slate: #5e7480;
    --nav-bg: #e8e8e8;
    --nav-active: #c9a2a4;
    --rule: #dcdcdc;
    --frame: #cfcfcf;
    --footer: #222a40;
    --arrow: #1f2238;
  }
  * { box-sizing: border-box; margin: 0; padding: 0; }
  html, body { width: 1200px; height: 954px; overflow: hidden; }
  body {
    background: var(--page-bg);
    font-family: "Source Sans 3", "PT Sans", sans-serif;
    color: var(--ink);
    position: relative;
  }
  .page-panel {
    position: absolute; left: 65px; top: 0; width: 1071px; height: 870px;
    background: var(--panel);
  }
  .brand {
    position: absolute; left: 96px; top: 40px; height: 52px;
    display: flex; align-items: center; gap: 10px; white-space: nowrap;
  }
  .brand-mark { width: 52px; height: 52px; background: var(--brand-slate); flex: none; }
  .brand-name {
    font-family: "Source Sans 3", sans-serif; font-weight: 400;
    font-size: 28px; letter-spacing: 0.5px; color: var(--brand-slate);
    white-space: nowrap;
  }
  .email-link {
    position: absolute; left: 984px; top: 21px;
    display: flex; align-items: center; gap: 8px;
    font-family: "PT Sans", sans-serif; font-size: 13.5px; letter-spacing: 0.8px;
    color: #444; text-decoration: none;
  }
  .search {
    position: absolute; left: 816px; top: 70px; width: 275px; height: 31px;
    border: 1px solid #cfcfcf; background: #fff;
    display: flex; align-items: center; justify-content: space-between;
    padding: 0 10px 0 12px;
    font-family: "PT Sans", sans-serif; font-size: 13px; color: #333;
  }
  .header-rule {
    position: absolute; left: 96px; top: 125px; width: 996px; height: 1px;
    background: var(--rule);
  }
  .main-nav { position: absolute; left: 0; top: 129px; width: 1200px; }
  .main-nav a {
    position: absolute; top: 0; width: 101px; height: 31px;
    border-radius: 4px; background: var(--nav-bg);
    font-family: "PT Sans", sans-serif; font-size: 15px; color: #222;
    text-decoration: none; display: flex; align-items: center; justify-content: center;
  }
  .main-nav a.is-active { background: var(--nav-active); }
  .slider-arrow { position: absolute; top: 323px; }
  .slider-frame {
    position: absolute; left: 155px; top: 186px; width: 881px; height: 344px;
    border: 4px solid var(--frame);
  }
  .slide-image {
    width: 100%; height: 100%;
    background: linear-gradient(180deg, #6f8fb8 0%, #b9b2a0 30%, #e8b451 45%, #5c5234 60%, #c99a56 72%, #5e4126 88%, #3a2b1d 100%);
  }
  .section-title {
    position: absolute; left: 152px; top: 548px; width: 888px; height: 33px;
    background: linear-gradient(180deg, #f2f2f2 0%, #ffffff 100%);
    padding-left: 21px; display: flex; align-items: center;
    font-family: "Source Sans 3", sans-serif; font-weight: 600; font-size: 18.5px;
    color: var(--heading);
  }
  .about-text {
    position: absolute; left: 158px; width: 885px;
    font-family: "PT Sans", sans-serif;
    font-size: 13.7px; line-height: 18.75px; letter-spacing: 0.2px;
  }
  .about-text.first { top: 598px; }
  .about-text.second { top: 735px; left: 159px; }
  .site-footer {
    position: absolute; left: 0; top: 870px; width: 1200px; height: 84px;
    background: var(--footer);
  }
  .social-links { position: absolute; left: 159px; top: 23px; display: flex; gap: 10px; }
  .social-links span { width: 40px; height: 40px; border-radius: 7px; display: block; }
  .social-feed { background: #e8642c; }
  .social-a { background: #3d6fb2; }
  .social-b { background: #2f7fb8; }
  .social-c { background: #c93a30; }
  .social-d { background: #5bb3cf; }
  .footer-brand {
    position: absolute; left: 888px; top: 12px; width: 246px; height: 62px;
    background: #fff; display: flex; align-items: center; justify-content: center;
    gap: 8px; white-space: nowrap; overflow: hidden;
  }
  .footer-brand .brand-mark { width: 40px; height: 40px; }
  .footer-brand .brand-name { font-size: 22px; }
</style>
</head>
<body>
  <div class="page-panel"></div>

  <header>
    <div class="brand"><span class="brand-mark"></span><span class="brand-name">Velmora Consulting</span></div>
    <a class="email-link" href="#">
      <svg width="26" height="26" viewBox="0 0 26 26" aria-hidden="true">
        <circle cx="13" cy="13" r="12" fill="#e6eef4" stroke="#c8d3dc"/>
        <text x="13" y="18.5" text-anchor="middle" font-family="PT Sans, sans-serif" font-size="17" font-weight="700" fill="#2a86c8">@</text>
      </svg>
      Email Us
    </a>
    <div class="search">
      <span>Search</span>
      <svg width="13" height="13" viewBox="0 0 13 13" aria-hidden="true">
        <circle cx="5" cy="5" r="3.8" fill="none" stroke="#777" stroke-width="1.6"/>
        <line x1="7.8" y1="7.8" x2="12" y2="12" stroke="#777" stroke-width="2"/>
      </svg>
    </div>
    <div class="header-rule"></div>
    <nav class="main-nav">
      <a href="#" style="left:264px">Home</a>
      <a href="#" class="is-active" style="left:378px">About</a>
      <a href="#" style="left:494px">Services</a>
      <a href="#" style="left:608px">Projects</a>
      <a href="#" style="left:723px">News</a>
      <a href="#" style="left:839px">Contacts</a>
    </nav>
  </header>

  <main>
    <svg class="slider-arrow" style="left:128px" width="21" height="56" viewBox="0 0 21 56" aria-label="Previous slide">
      <polygon points="21,0 0,28 21,56 15,28" fill="var(--arrow)"/>
    </svg>
    <div class="slider-frame">
      <div class="slide-image" role="img" aria-label="Lakeside sunset with a windswept tree, mountains and still water"></div>
    </div>
    <svg class="slider-arrow" style="left:1041px" width="21" height="56" viewBox="0 0 21 56" aria-label="Next slide">
      <polygon points="0,0 21,28 0,56 6,28" fill="var(--arrow)"/>
    </svg>

    <h1 class="section-title">About Us</h1>
    <p class="about-text first">Velmora Consulting is a firm specialized in providing customized Organization Development solutions to companies in the Middle East and Africa. Recognizing the inability of imported models and solutions to solve problems that face companies in our region, Velmora Consulting builds on international best practices and customizes them to create best-fit solutions that are capable of addressing challenges effectively.Velmora Consulting provides Organization Development solutions addressing the "HOW – Soft Side" that is needed to achieve the "WHAT – Business Strategy" in a holistic manner. Velmora Consulting work centers around building an organizational culture that is aligned with and supports the business strategy.</p>
    <p class="about-text second">Velmora Consulting is a firm specialized in providing customized Organization Development solutions to companies in the Middle East and Africa. Recognizing the inability of imported models and solutions to solve problems that face companies in our region, Velmora Consulting builds on international best practices and customizes them to create best-fit solutions that are capable of addressing challenges effectively.</p>
  </main>

  <footer class="site-footer">
    <div class="social-links">
      <span class="social-feed" aria-label="News feed"></span>
      <span class="social-a" aria-label="Social profile"></span>
      <span class="social-b" aria-label="Professional network"></span>
      <span class="social-c" aria-label="Video channel"></span>
      <span class="social-d" aria-label="Microblog"></span>
    </div>
    <div class="footer-brand"><span class="brand-mark"></span><span class="brand-name">Velmora Consulting</span></div>
  </footer>
</body>
</html>
```